New design for www.TrimSlotly.com

On TrimSlotly you can find & book your hairdresser. TrimSlotly is the biggest platform in the Netherlands.

- The design should be a responcive design
- Should be able to go global, should fit in perfectly between all the big booking platforms like roomqy, zipto etc,
- Should have te result of more bookings. :)
- We are ‘only’ asking a beautiful design, not a technical solution.
- We need a homepage (https://trimslotly.com/), search resultpage ((https://trimslotly.com/kapper/amsterdam/#), salonpage (https://trimslotly.com/kapper/vorden/mirelle-salon-studio/), about us page (https://trimslotly.com/aboutus/), for the hairdresser info page (https://trimslotly.com/kapper/), login/register page (https://trimslotly.com/account/signin/).

- On the page of the hairdresser there is a dynamic part. The part where you create your appointment. Please take a look at this part too after you choose your treatment (behandeling), employee (medewerker), Date (datum) and time (tijd). The part that you see after this, is the part where you fill in your data as a consumer.

I've added more logo's but mostly we use the green color.

A few of our competitors: www.glossmora.com, www.pelikora.com

Target Market(s)

All consumers

Industry/Entity Type

Hair And Beauty

Number of Pages Required

5+ page

Font styles to use
Sans Serif

Colors
abd036
c3c3c3
757575

Requirements
Must have
• Responsive
• We did an A/B test with the homepage. It turns out that option B works better then option A (take a look at the uploaded pictures). So what we need on the homepage: The USP's with the green checkboxes, The search button needs to by dynamic (changes for example from light green to dark green so you can see you can click it) The call to action sentence Zoek & Vind je kapsalon, the searchfield and searchbutton should be seperated.
Nice to have
• The style that we like is the flat design style. The website should be simple, clean and it should feel a bit like a luxury thing. Because an appointment with the hairdresser can be a real treat and luxury moment for yourself.
• The luxury feeling and flat design that is in the www.zipto.com website is really nice for example. But then it has to be a bit more light and not so black and dark.

```html
<!DOCTYPE html>
<html lang="en">
<head>
<meta charset="utf-8">
<title>TrimSlotly – Find &amp; book your hairdresser</title>
<link href="https://fonts.googleapis.com/css2?family=Roboto:wght@300;400;500;700&family=Roboto+Condensed:wght@400;700&display=swap" rel="stylesheet">
<style>
:root{
  --green:#abd036;
  --green-dark:#8fb224;
  --grey-light:#c3c3c3;
  --grey:#757575;
  --ink:#3d4650;
  --footer:#4b5662;
  --footer-dark:#3c4650;
  --paper:#ffffff;
  --mist:#f3f4f4;
  --badge:#1e2326;
}
*{box-sizing:border-box;margin:0;padding:0}
html,body{width:1200px;height:2792px;overflow:hidden}
body{font-family:'Roboto',Arial,sans-serif;color:var(--ink);background:var(--paper);position:relative}
a{color:inherit;text-decoration:none}

/* hero */
.hero{position:absolute;left:0;top:0;width:1200px;height:620px;
  background:linear-gradient(90deg,#2f3a3f 0%,#4f5c5f 45%,#8a8577 75%,#b9a690 100%);overflow:hidden}
.hero-photo{position:absolute;inset:0;background:radial-gradient(ellipse at 78% 55%,rgba(210,180,150,.55),rgba(0,0,0,0) 60%)}
.hero-shade{position:absolute;inset:0;background:rgba(20,28,32,.35)}
.topbar{position:absolute;left:0;top:0;width:1200px;height:64px;display:flex;align-items:center;justify-content:space-between;padding:0 100px}
.brand{display:flex;align-items:center;gap:10px;color:#fff;font-weight:500;font-size:26px}
.brand-dot{width:22px;height:22px;border-radius:50%;background:#fff}
.account-links{display:flex;gap:10px}
.account-links a{border:1px solid rgba(255,255,255,.7);color:#fff;font-size:12px;letter-spacing:1px;padding:6px 14px;text-transform:uppercase}
.hero-title{position:absolute;top:168px;width:100%;text-align:center;color:#fff;font-family:'Roboto Condensed',Arial,sans-serif;font-weight:700;font-size:66px;letter-spacing:2px}
.hero-sub{position:absolute;top:262px;width:100%;text-align:center;color:#fff;font-size:17px;font-weight:500;letter-spacing:.5px;text-transform:uppercase}
.search{position:absolute;top:338px;left:340px;display:flex;gap:12px}
.search input{width:320px;height:46px;border:0;padding:0 16px;font:400 14px 'Roboto',Arial,sans-serif;color:var(--grey)}
.search .select{width:130px;height:46px;background:#fff;color:var(--grey);font-size:14px;display:flex;align-items:center;justify-content:space-between;padding:0 14px}
.search button{width:78px;height:46px;border:0;background:var(--green);color:#fff;font:500 14px 'Roboto',Arial,sans-serif;text-transform:uppercase;cursor:pointer}
.search button:hover{background:var(--green-dark)}
.hero-alt{position:absolute;top:410px;width:100%;text-align:center;color:#fff;font-size:13px;letter-spacing:1px;text-transform:uppercase;opacity:.9}

/* intro */
.intro{position:absolute;top:620px;left:0;width:1200px;height:540px;background:var(--paper)}
.intro h2{position:absolute;top:42px;width:100%;text-align:center;font-weight:400;font-size:44px;color:#5a7a7a}
.intro .latest{position:absolute;top:104px;width:100%;text-align:center;color:var(--green);font-size:17px}
.laptop{position:absolute;left:150px;top:200px;width:400px;height:270px}
.features{position:absolute;left:590px;top:206px;width:500px;display:grid;grid-template-columns:1fr 1fr;row-gap:36px;column-gap:30px}
.feature{display:flex;gap:14px}
.feature-icon{width:44px;height:44px;background:#5b6670;flex:none;display:flex;align-items:center;justify-content:center}
.feature h3{font-size:16px;font-weight:500;color:var(--ink);margin-bottom:4px}
.feature p{font-size:12px;line-height:17px;color:var(--grey)}

/* app band */
.app-band{position:absolute;top:1160px;left:0;width:1200px;height:480px;background:var(--green)}
.app-notch{position:absolute;left:560px;top:0}
.phones{position:absolute;left:210px;top:56px;width:300px;height:380px}
.app-copy{position:absolute;left:630px;top:118px;color:#fff;width:420px}
.app-copy h2{font-family:'Roboto Condensed',Arial,sans-serif;font-size:40px;font-weight:700;letter-spacing:.5px}
.app-copy .lead{font-size:24px;font-weight:300;margin-top:2px}
.app-copy p{font-size:13px;line-height:19px;margin-top:14px;opacity:.95}
.badges{display:flex;gap:12px;margin-top:18px}
.badge{width:140px;height:44px;background:var(--badge);border-radius:6px;display:flex;align-items:center;justify-content:center;gap:10px;color:#fff;font-size:15px;font-weight:500}
.badge-dot{width:18px;height:18px;border-radius:50%;background:#fff;flex:none}
.app-button{display:inline-block;margin-top:18px;border:1px solid #fff;color:#fff;font-size:12px;letter-spacing:1px;padding:10px 22px;text-transform:uppercase}

/* steps */
.steps{position:absolute;top:1640px;left:0;width:1200px;height:480px;background:var(--mist)}
.steps h2{position:absolute;top:60px;width:100%;text-align:center;font-size:32px;font-weight:400;color:var(--ink);text-transform:uppercase}
.steps-line{position:absolute;left:260px;top:250px}
.step{position:absolute;top:148px;width:260px;text-align:center}
.step h3{margin-top:20px;font-size:15px;font-weight:500;color:var(--ink)}
.step p{margin-top:8px;font-size:12px;line-height:17px;color:var(--grey)}

/* newsletter */
.tips{position:absolute;top:2120px;left:0;width:1200px;height:340px;background:linear-gradient(90deg,#eeeeec 0%,#f6f5f2 50%,#e3ddd6 100%)}
.tips h2{position:absolute;top:70px;width:100%;text-align:center;font-family:'Roboto Condensed',Arial,sans-serif;font-weight:700;font-size:38px;color:var(--ink);text-transform:uppercase}
.tips p{position:absolute;top:134px;width:100%;text-align:center;font-size:14px;line-height:20px;color:var(--green)}
.tips form{position:absolute;top:200px;left:230px;display:flex;gap:14px}
.tips input{width:560px;height:50px;border:0;background:#fff;padding:0 18px;font:400 13px 'Roboto',Arial,sans-serif;color:var(--grey)}
.tips button{width:150px;height:50px;border:0;background:var(--green);color:#fff;font:500 15px 'Roboto',Arial,sans-serif;text-transform:uppercase}

/* footer */
.site-footer{position:absolute;top:2460px;left:0;width:1200px;height:300px;background:var(--footer);color:#dfe3e6}
.footer-brand{position:absolute;left:100px;top:36px;display:flex;flex-direction:column;align-items:center;gap:10px}
.footer-brand .mark{width:70px;height:70px;background:var(--green)}
.footer-brand span{font-size:16px;font-weight:500;color:#fff}
.footer-col{position:absolute;top:40px;font-size:12px;line-height:20px}
.footer-col h4{font-size:13px;font-weight:500;color:#fff;text-transform:uppercase;margin-bottom:8px;letter-spacing:.5px}
.social li{display:flex;align-items:center;gap:10px;margin-bottom:8px}
.social i{width:22px;height:22px;border-radius:50%;border:1px solid #aab3ba;display:inline-block}
ul{list-style:none}
.copyright{position:absolute;top:2760px;left:0;width:1200px;height:32px;background:var(--footer-dark);color:#aab3ba;font-size:11px;text-align:center;line-height:32px}
</style>
</head>
<body>

<header class="hero">
  <div class="hero-photo" role="img" aria-label="Photo of a smiling client at a hairdresser's salon"></div>
  <div class="hero-shade"></div>
  <div class="topbar">
    <a class="brand" href="https://trimslotly.com/"><span class="brand-dot"></span>TrimSlotly</a>
    <nav class="account-links"><a href="https://trimslotly.com/account/signin/">Sign in</a><a href="https://trimslotly.com/account/signin/">Register</a></nav>
  </div>
  <h1 class="hero-title">TRIMSLOTLY</h1>
  <p class="hero-sub">The greatest hairdresser booking site in the Netherlands with 1461 hairdressers</p>
  <form class="search">
    <input type="text" placeholder="Find a place or postcode">
    <div class="select">All cities
      <svg width="10" height="6" viewBox="0 0 10 6"><path d="M0 0h10L5 6z" fill="#757575"/></svg></div>
    <button type="button">Search</button>
  </form>
  <a class="hero-alt" href="#">Or search salon name</a>
</header>

<section class="intro">
  <h2>TrimSlotly</h2>
  <p class="latest">Last appointment on October 15, 2015 at 17:09</p>
  <svg class="laptop" viewBox="0 0 400 270" role="img" aria-label="Laptop showing the booking site">
    <rect x="40" y="0" width="320" height="220" rx="10" fill="#2b3035"/>
    <rect x="56" y="16" width="288" height="188" fill="var(--green)"/>
    <rect x="0" y="222" width="400" height="16" rx="4" fill="#d5d8da"/>
    <rect x="160" y="222" width="80" height="6" fill="#b8bdc0"/>
  </svg>
  <div class="features">
    <div class="feature"><div class="feature-icon"><svg width="22" height="22" viewBox="0 0 22 22"><rect x="2" y="2" width="8" height="8" fill="#fff"/><rect x="12" y="2" width="8" height="8" fill="#fff"/><rect x="2" y="12" width="8" height="8" fill="#fff"/><rect x="12" y="12" width="8" height="8" fill="#fff"/></svg></div><div><h3>salons</h3><p>Every salon near you listed<br>with prices and photos</p></div></div>
    <div class="feature"><div class="feature-icon"><svg width="22" height="22" viewBox="0 0 22 22"><path d="M3 11l5 5L19 5" stroke="#fff" stroke-width="3" fill="none"/></svg></div><div><h3>agreements</h3><p>Clear terms for every visit,<br>confirmed right away</p></div></div>
    <div class="feature"><div class="feature-icon"><svg width="22" height="22" viewBox="0 0 22 22"><path d="M2 18L9 10l4 4 7-9" stroke="#fff" stroke-width="2.5" fill="none"/></svg></div><div><h3>Treatments for booking</h3><p>Cuts, colour and styling<br>ready to book online</p></div></div>
    <div class="feature"><div class="feature-icon"><svg width="22" height="22" viewBox="0 0 22 22"><rect x="3" y="4" width="16" height="15" fill="none" stroke="#fff" stroke-width="2"/><path d="M3 9h16" stroke="#fff" stroke-width="2"/></svg></div><div><h3>hairdressers booking</h3><p>Pick your stylist and time<br>in a few simple clicks</p></div></div>
    <div class="feature"><div class="feature-icon"><svg width="22" height="22" viewBox="0 0 22 22"><circle cx="11" cy="11" r="8" fill="none" stroke="#fff" stroke-width="2"/><circle cx="11" cy="11" r="3" fill="#fff"/></svg></div><div><h3>Reliable reviews</h3><p>Honest ratings from real<br>clients after each visit</p></div></div>
  </div>
</section>

<section class="app-band">
  <svg class="app-notch" width="80" height="30" viewBox="0 0 80 30"><path d="M0 0h80L40 30z" fill="#fff"/></svg>
  <svg class="phones" viewBox="0 0 300 380" role="img" aria-label="Two phones showing the TrimSlotly app">
    <rect x="0" y="60" width="150" height="300" rx="18" fill="#f2f2f2"/>
    <rect x="12" y="100" width="126" height="220" fill="#dfe6c4"/>
    <rect x="110" y="0" width="170" height="350" rx="22" fill="#1e2326"/>
    <rect x="122" y="48" width="146" height="256" fill="#ffffff"/>
    <rect x="122" y="48" width="146" height="40" fill="var(--green)"/>
  </svg>
  <div class="app-copy">
    <h2>ALL THE HAIRDRESSERS</h2>
    <div class="lead">of Netherlands in your pocket!</div>
    <p>Download the TrimSlotly app and always find a salon<br>to book a quick trim on the go.</p>
    <div class="badges">
      <a class="badge" href="#"><span class="badge-dot"></span>App Shelf</a>
      <a class="badge" href="#"><span class="badge-dot"></span>Play Shelf</a>
    </div>
    <a class="app-button" href="#">Download Android App</a>
  </div>
</section>

<section class="steps">
  <h2>How does it work?</h2>
  <svg class="steps-line" width="680" height="4"><line x1="0" y1="2" x2="680" y2="2" stroke="#c3c3c3" stroke-width="2"/></svg>
  <div class="step" style="left:200px">
    <svg width="110" height="140" viewBox="0 0 110 140"><path d="M55 136C55 136 8 78 8 52a47 47 0 0 1 94 0c0 26-47 84-47 84z" fill="#fff" stroke="var(--green)" stroke-width="3"/><circle cx="51" cy="50" r="15" fill="none" stroke="var(--green)" stroke-width="4"/><path d="M62 61l12 12" stroke="var(--green)" stroke-width="5"/></svg>
    <h3>Search &amp; Find hairdresser</h3>
    <p>Enter your city or postcode and<br>see every salon nearby at once.</p>
  </div>
  <div class="step" style="left:470px">
    <svg width="110" height="140" viewBox="0 0 110 140"><path d="M55 136C55 136 8 78 8 52a47 47 0 0 1 94 0c0 26-47 84-47 84z" fill="#fff" stroke="var(--green)" stroke-width="3"/><rect x="36" y="36" width="38" height="26" fill="none" stroke="var(--green)" stroke-width="3"/><path d="M30 66h50" stroke="var(--green)" stroke-width="4"/></svg>
    <h3>Book your appointment<br>online with 100% certainty</h3>
    <p>Choose a treatment, stylist and time<br>and get your confirmation directly.</p>
  </div>
  <div class="step" style="left:740px">
    <svg width="110" height="140" viewBox="0 0 110 140"><path d="M55 136C55 136 8 78 8 52a47 47 0 0 1 94 0c0 26-47 84-47 84z" fill="#fff" stroke="var(--green)" stroke-width="3"/><circle cx="55" cy="50" r="18" fill="none" stroke="var(--green)" stroke-width="3"/><path d="M46 55q9 8 18 0" stroke="var(--green)" stroke-width="3" fill="none"/><circle cx="48" cy="45" r="2.5" fill="var(--green)"/><circle cx="62" cy="45" r="2.5" fill="var(--green)"/></svg>
    <h3>Enjoy your new hairstyle</h3>
    <p>Relax in the chair and treat yourself,<br>then leave a review afterwards.</p>
  </div>
</section>

<section class="tips" role="img" aria-label="Soft salon interior backdrop for the newsletter">
  <h2>Nice TrimSlotly get tips?</h2>
  <p>Subscribe to our newsletter to be notified<br>about new salons nearby</p>
  <form><input type="email" placeholder="Enter your E-mail address"><button type="button">Sign up</button></form>
</section>

<footer class="site-footer">
  <div class="footer-brand"><span class="mark"></span><span>TrimSlotly</span></div>
  <div class="footer-col" style="left:330px"><h4>Quick links</h4><ul><li>Salon Amsterdam</li><li>Salon Rotterdam</li><li>Salon Utrecht</li><li>Salon Den Haag</li><li>Salon Eindhoven</li></ul></div>
  <div class="footer-col" style="left:530px"><h4>TrimSlotly</h4><ul><li>salons</li><li>Treatments for booking</li><li>agreements</li><li>hairdressers booking</li><li>Website review</li></ul></div>
  <div class="footer-col social" style="left:740px"><h4>Offering</h4><ul><li><i></i>Circlebook</li><li><i></i>Chirply</li><li><i></i>Plusgrid</li></ul></div>
  <div class="footer-col" style="left:940px"><h4>Contact us</h4><ul><li>TrimSlotly</li><li>2611 KT, Delft</li><li>&nbsp;</li><li>+31 15 555 0142</li><li>info@trimslotly.com</li></ul></div>
</footer>
<div class="copyright">Copyright 2015 TrimSlotly</div>

</body>
</html>
```